Print and eBook Cover Design for American Police Book

I need a book cover (front, spine, and back) designed for my completed book. The cover needs to be 5 x 8 and will be uploaded to Pellorin. The title is:

Steady Hands at Dawn: Gentle Accounts from Ordinary Patrol Deputies.

This book is a compilation of positive, uplifting stories of Police Officers going above and beyond to serve their communities. This book is being published to combat the negative news and social media stories that flood the internet.

The interior is currently being formatted but it looks as if the book will be around 162 pages.

Target Market(s)

This book is intended to target people who love law and order and who support police in America.

Industry/Entity Type

Book Publisher

Colors
000000
0456a4
33a6d7

Requirements
Must have
• I am not an artistic person so I don't have a solid idea of what the cover should look like. Here's what I'd like to see...

An American Flag (possible waving)
A police officer saluting or maybe the sillouhette of an officer on the cover (this is not a must but might look nice)
Possibly a police badge or a police patch
Possibly a police brevant or police car with red and blue lights activated
Possibly a police statue or picture of a police memorial

The color blue represents police officers so that is a must.

I would also like to have 'Foreword by Joy Tremwick' on the front cover.

Like I said above, I am not an artist so I will be relying heavily on opinions from the pros. I have the back of book blurb completed and can upload that when necessary.

Author name is Dustin Ferrow
Nice to have
• possibly a thin blue line symbol

This book is similar to the Warm Bread by the Window books. It's a bunch of feel good stories about American police officers. Anything I didn't mention that seems like a good idea is welcome.
Should not have
• Should not have anything negative toward police.

```html
<!DOCTYPE html>
<html lang="en">
<head>
<meta charset="utf-8">
<title>Steady Hands at Dawn – Full Cover</title>
<link rel="stylesheet" href="https://fonts.googleapis.com/css2?family=Anton&family=Bebas+Neue&family=Oswald:wght@300;600&family=Roboto:wght@400;500&display=swap">
<style>
  :root {
    --ink: #000000;
    --paper: #ffffff;
    --police-blue: #33a6d7;
    --deep-blue: #0456a4;
    --night: #0a0a2a;
    --flag-grey: #8a8a8a;
  }
  html, body {
    margin: 0;
    padding: 0;
    width: 1200px;
    height: 960px;
    overflow: hidden;
    background: var(--paper);
  }
  .cover {
    position: relative;
    width: 1200px;
    height: 960px;
    overflow: hidden;
    font-family: "Roboto", Arial, sans-serif;
  }

  /* ---------- Back cover ---------- */
  .back {
    position: absolute;
    left: 0; top: 0;
    width: 576px; height: 960px;
    background: linear-gradient(to bottom,
      var(--ink) 0, var(--ink) 490px,
      #f4f4f4 560px, var(--paper) 600px, var(--paper) 100%);
  }
  .back-footer-band {
    position: absolute;
    left: 0; top: 860px;
    width: 576px; height: 100px;
    background: var(--ink);
  }
  .back-title {
    position: absolute;
    left: 0; top: 16px;
    width: 576px;
    margin: 0;
    text-align: center;
    font-family: "Anton", Impact, sans-serif;
    font-weight: 400;
    font-size: 60px;
    line-height: 76px;
    color: var(--paper);
    letter-spacing: 0.5px;
  }
  .back-subtitle {
    position: absolute;
    left: 0; top: 96px;
    width: 576px;
    margin: 0;
    text-align: center;
    font-family: "Oswald", "Arial Narrow", sans-serif;
    font-weight: 600;
    font-size: 19px;
    color: var(--paper);
  }
  .blurb {
    position: absolute;
    left: 34px;
    width: 510px;
    margin: 0;
    font-size: 15.6px;
    line-height: 24px;
    color: var(--paper);
  }
  .blurb-one { top: 152px; }
  .blurb-two { top: 349px; }

  .author-photo {
    position: absolute;
    left: 34px; top: 558px;
    width: 112px; height: 132px;
    background: var(--ink);
    color: var(--paper);
    font-size: 12.5px;
    display: flex;
    align-items: center;
    justify-content: center;
  }
  .author-bio {
    position: absolute;
    left: 158px; top: 562px;
    width: 392px;
    margin: 0;
    font-size: 15.6px;
    line-height: 24px;
    color: var(--ink);
  }
  .author-bio-cont {
    position: absolute;
    left: 34px; top: 692px;
    width: 510px;
    margin: 0;
    font-size: 15.6px;
    line-height: 24px;
    color: var(--ink);
  }
  .publisher-mark {
    position: absolute;
    left: 34px; top: 826px;
    font-family: "Roboto", Arial, sans-serif;
    font-weight: 500;
    font-size: 28px;
    color: var(--ink);
  }
  .isbn-box {
    position: absolute;
    left: 310px; top: 790px;
    width: 239px; height: 142px;
    background: var(--police-blue);
  }

  /* ---------- Spine + front imagery ---------- */
  .flag-photo {
    position: absolute;
    left: 576px; top: 0;
    width: 624px; height: 500px;
    background:
      linear-gradient(to bottom, rgba(0,0,0,0) 60%, rgba(0,0,0,0.9) 100%),
      linear-gradient(170deg, #2a2a2a 0%, #9a9a9a 20%, #3a3a3a 35%, #b0b0b0 48%, #1f3f8a 56%, #2a58b8 60%, #3a3a3a 70%, #8c8c8c 82%, #1a1a1a 100%);
  }
  .lights-photo {
    position: absolute;
    left: 576px; top: 470px;
    width: 624px; height: 490px;
    background:
      radial-gradient(ellipse 140px 80px at 390px 110px, rgba(220,230,255,0.95), rgba(40,80,255,0.6) 50%, rgba(0,0,0,0) 100%),
      radial-gradient(ellipse 120px 70px at 220px 90px, rgba(230,70,170,0.8), rgba(0,0,0,0) 100%),
      radial-gradient(ellipse 160px 120px at 560px 140px, rgba(200,40,90,0.6), rgba(0,0,0,0) 100%),
      radial-gradient(ellipse 300px 60px at 330px 300px, rgba(180,190,220,0.5), rgba(0,0,0,0) 100%),
      linear-gradient(to bottom, #0a0a28 0%, #141450 40%, #0a0a1e 75%, #000000 100%);
  }

  .spine-title, .spine-author {
    position: absolute;
    left: 620px;
    margin: 0;
    transform-origin: 0 0;
    transform: rotate(90deg);
    white-space: nowrap;
    font-family: "Bebas Neue", Impact, sans-serif;
    font-size: 44px;
    line-height: 44px;
    color: var(--paper);
  }
  .spine-title { top: 18px; }
  .spine-author { top: 690px; }

  /* ---------- Front cover ---------- */
  .front-title {
    position: absolute;
    left: 688px; top: 14px;
    margin: 0;
    font-family: "Anton", Impact, sans-serif;
    font-weight: 400;
    color: var(--police-blue);
    line-height: 1;
  }
  .title-line {
    display: block;
    font-size: 146px;
    line-height: 152px;
    letter-spacing: -1px;
  }
  .title-turned {
    position: absolute;
    left: 445px; top: 8px;
    transform-origin: 0 0;
    transform: rotate(90deg) translateY(-100%);
    font-size: 70px;
    line-height: 62px;
    color: var(--paper);
    white-space: nowrap;
  }
  .front-subtitle {
    position: absolute;
    left: 640px; top: 358px;
    width: 540px;
    margin: 0;
    text-align: center;
    font-family: "Oswald", "Arial Narrow", sans-serif;
    font-weight: 600;
    font-size: 27px;
    line-height: 32px;
    color: var(--paper);
  }
  .front-author {
    position: absolute;
    left: 640px; top: 834px;
    width: 540px;
    margin: 0;
    text-align: center;
    font-family: "Bebas Neue", Impact, sans-serif;
    font-size: 78px;
    line-height: 72px;
    color: var(--paper);
  }
  .front-foreword {
    position: absolute;
    left: 640px; top: 900px;
    width: 540px;
    margin: 0;
    text-align: center;
    font-family: "Oswald", "Arial Narrow", sans-serif;
    font-weight: 300;
    font-size: 30px;
    line-height: 38px;
    color: var(--paper);
  }
</style>
</head>
<body>
<main class="cover">

  <section class="back">
    <h2 class="back-title">STEADY HANDS AT DAWN</h2>
    <p class="back-subtitle">GENTLE ACCOUNTS FROM ORDINARY PATROL DEPUTIES</p>

    <p class="blurb blurb-one">Lorem ipsum dolor sit amet, consectetur adipisicing elit, sed do eiusmod tempor incididunt ut labore et dolore magna aliqua. Ut enim ad minim veniam, quis nostrud exercitation ullamco laboris nisi ut aliquip ex ea commodo consequat. Duis aute irure dolor in reprehenderit in voluptate velit esse cillum dolore eu fugiat nulla pariatur. Excepteur sint occæcat cupidatat non proident, sunt in culpa qui officia deserunt mollit anim id est laborum.</p>
    <p class="blurb blurb-two">Sed ut perspiciatis unde omnis iste natus error sit voluptatem accusantium doloremque laudantium, totam rem aperiam, eaque ipsa quæ ab illo inventore veritatis et quasi architecto beatæ vitæ dicta sunt explicabo. Nemo enim ipsam voluptatem quia voluptas sit aspernatur aut odit aut fugit, sed quia consequuntur magni dolores eos qui ratione voluptatem sequi nesciunt.</p>

    <div class="back-footer-band"></div>

    <div class="author-photo" role="img" aria-label="Author portrait placeholder">Author's picture</div>
    <p class="author-bio">Lorem ipsum dolor sit amet, consectetur adipisicing elit, sed do eiusmod tempor incididunt ut labore et dolore magna aliqua. Ut enim ad minim veniam, quis nostrud exercitation ullamco laboris nisi ut aliquip ex ea commodo consequat.</p>
    <p class="author-bio-cont">Duis aute irure dolor in reprehenderit in voluptate velit esse cillum dolore eu fugiat nulla pariatur. Excepteur sint occæcat cupidatat non proident, sunt in culpa qui officia deserunt mollit anim id est laborum.</p>

    <div class="publisher-mark">Pellorin</div>
    <div class="isbn-box"></div>
  </section>

  <div class="flag-photo" role="img" aria-label="Waving black and white American flag with a thin blue line stripe"></div>
  <div class="lights-photo" role="img" aria-label="Police car roof with red and blue emergency lights glowing at night"></div>

  <p class="spine-title">STEADY HANDS AT DAWN</p>
  <p class="spine-author">AUTHOR'S NAME</p>

  <section class="front">
    <h1 class="front-title">
      <span class="title-line">STEADY</span>
      <span class="title-line">AT DAWN</span>
      <span class="title-turned">HANDS</span>
    </h1>
    <p class="front-subtitle">GENTLE ACCOUNTS FROM ORDINARY<br>PATROL DEPUTIES</p>
    <p class="front-author">DUSTIN FERROW</p>
    <p class="front-foreword">FOREWORD BY JOY TREMWICK</p>
  </section>

</main>
</body>
</html>
```